Sheep ranch business card design

We need a business card design for our farm. We do all things sheep. We run Babydoll southdown sheep and use their fiber and meat. In the spring the lambs are sold. We shear them for their wool to make dryer balls, roving, and yarn which we sell. We also lease the sheep out to organic vineyards in the winter time to help them convert their weeds and cover crops to manure so they don't have to use tractors and tillers to mow and compact soil. Copperfield Ranch also breeds Kangals which are livestock guard dogs that live with and protect the sheep. We also run a small herd of jersey cows, chickens, and bees but the sheep enterprise is the focal point. I would like to see the design use more earth tones and natural colors and have the feel of a modern and hip farm. I would also like our attached copperfield ranch image to be used. The font family is dalle for our logo. That font can be used or something to compliment it. The attached pictures can be used as well but they are not necessary. One copperfield ranch upload is in psd and one is in jpeg. Thank You and we look forward to seeing your work.
Updates

So many great designs. Not looking for anything "western." Font, design, or otherwise.

Industry/Entity Type

Livestock

Contact Information for Business Card

Copperfield Ranch
Tessa Pollard
www.copperfieldranch.example
copperfieldranch@mailbox.example
phone: 555 210-7389

```html
<!DOCTYPE html>
<html lang="en">
<head>
<meta charset="utf-8">
<title>Copperfield Ranch – Business Card</title>
<link href="https://fonts.googleapis.com/css2?family=Cormorant+SC:wght@500;600&family=Crimson+Text&display=swap" rel="stylesheet">
<style>
  :root {
    --backdrop: #e4e2dc;
    --harvest-gold: #cfa52c;
    --pasture-dark: #2f4a1f;
    --pasture-band: #3b8a3a;
    --ink: #2b2a26;
    --cream: #f3ecd6;
    --fleece: #d9d6cc;
    --shadow: rgba(0,0,0,.18);
  }
  * { margin: 0; padding: 0; box-sizing: border-box; }
  html, body { width: 1200px; height: 873px; overflow: hidden; }
  body {
    background: var(--backdrop);
    display: flex; align-items: center; justify-content: center;
  }
  .business-card {
    position: relative;
    width: 1000px; height: 572px;
    background: var(--harvest-gold);
    overflow: hidden;
    box-shadow: 0 10px 30px var(--shadow);
  }
  .pasture-shape { position: absolute; inset: 0; width: 100%; height: 100%; }
  .brand {
    position: absolute; top: 62px; left: 440px; width: 540px;
    text-align: center; white-space: nowrap;
    font-family: "Cormorant SC", serif; font-weight: 600;
    font-size: 42px; letter-spacing: 2px; color: var(--ink);
  }
  .people {
    position: absolute; top: 140px; left: 480px; width: 480px;
    display: flex; justify-content: space-between;
    font-family: "Cormorant SC", serif; font-weight: 500;
    font-size: 28px; color: var(--cream); letter-spacing: 1px;
    list-style: none; white-space: nowrap;
  }
  .contact-list {
    position: absolute; left: 40px; top: 50px;
    list-style: none;
    font-family: "Crimson Text", serif; font-size: 20px; color: var(--cream);
  }
  .contact-list li { display: flex; align-items: center; gap: 12px; line-height: 36px; white-space: nowrap; }
  .contact-icon { width: 18px; height: 18px; flex: none; }
  .sheep {
    position: absolute; background: linear-gradient(180deg, #eeebe3, var(--fleece));
    border-radius: 40% 45% 30% 30%;
  }
  .sheep-large { left: 520px; top: 370px; width: 170px; height: 100px; }
  .sheep-small { left: 740px; top: 440px; width: 130px; height: 85px; }
</style>
</head>
<body>
  <article class="business-card">
    <svg class="pasture-shape" viewBox="0 0 1000 572" preserveAspectRatio="none" aria-hidden="true">
      <path d="M0 0 H420 C450 200 700 330 1000 380 V572 H0 Z" fill="var(--pasture-band)"/>
      <path d="M0 0 H395 C420 220 680 360 1000 410 V572 H0 Z" fill="var(--pasture-dark)"/>
    </svg>

    <header class="brand">Copperfield Ranch</header>

    <ul class="people">
      <li>Tessa Pollard</li>
      <li>Dale Pollard</li>
    </ul>

    <ul class="contact-list">
      <li>
        <svg class="contact-icon" viewBox="0 0 24 24" aria-hidden="true"><rect x="2" y="5" width="20" height="14" rx="2" fill="var(--harvest-gold)"/><path d="M3 6 L12 13 L21 6" fill="none" stroke="var(--pasture-dark)" stroke-width="2"/></svg>
        copperfieldranch@mailbox.example
      </li>
      <li>
        <svg class="contact-icon" viewBox="0 0 24 24" aria-hidden="true"><path d="M6 2 L10 2 L11 7 L8 9 C9 12 12 15 15 16 L17 13 L22 14 L22 18 C22 20 20 22 18 22 C9 21 3 15 2 6 C2 4 4 2 6 2 Z" fill="var(--harvest-gold)"/></svg>
        555 210-7389
      </li>
      <li>
        <svg class="contact-icon" viewBox="0 0 24 24" aria-hidden="true"><circle cx="12" cy="12" r="9" fill="none" stroke="var(--harvest-gold)" stroke-width="2"/><path d="M3 12 H21 M12 3 C7 8 7 16 12 21 M12 3 C17 8 17 16 12 21" fill="none" stroke="var(--harvest-gold)" stroke-width="1.6"/></svg>
        www.copperfieldranch.example
      </li>
    </ul>

    <div class="sheep sheep-large" role="img" aria-label="Engraved illustration of a standing sheep"></div>
    <div class="sheep sheep-small" role="img" aria-label="Engraved illustration of a lamb"></div>
  </article>
</body>
</html>
```